Geschäftspapiere für eine Zahnarztpraxis
Zielgruppe
Zahnarztpraxis
Aufgabenstellung
Ich wünsche mir wenige grafische Elemente auf der Vorderseite. Die Rückseite soll komplett mit einer Grafik gefüllt sein.
Die Datei die ich als Fototapete zur Verfügung stelle, muss nicht zwangsläufig in dem Designvorschlag enthalten sein. Die Tapeten machen einen Großteil der Inneneinrichtung meiner Praxis aus. Sie sind ein Wiedererkennungsmerkmal, daher dachte ich, es würde Sinn ergeben, diese zum Teil in das Design einfließen zu lassen.

```html
<!DOCTYPE html>
<html lang="de">
<head>
<meta charset="utf-8">
<title>Geschäftsausstattung Zahnarztpraxis Halvering &amp; Team</title>
<link href="https://fonts.googleapis.com/css2?family=Figtree:wght@300;400;600&display=swap" rel="stylesheet">
<style>
  :root{
    --stage:#8faba5;
    --paper:#ffffff;
    --teal:#3f7a6d;
    --teal-soft:#6f9c92;
    --band:#e0e6e4;
    --ink:#555b5a;
    --rule:#9aa7a4;
  }
  *{box-sizing:border-box;margin:0;padding:0}
  html,body{width:1200px;height:1200px;overflow:hidden}
  body{background:var(--stage);font-family:"Figtree",sans-serif;color:var(--ink);position:relative}

  .letterhead{position:absolute;left:73px;top:50px;width:780px;height:1103px;background:var(--paper);box-shadow:0 2px 6px rgba(0,0,0,.15);overflow:hidden}
  .brand{position:absolute;left:74px;top:56px;display:flex;align-items:center;gap:14px}
  .brand-dot{width:44px;height:44px;border:1.5px solid var(--teal);border-radius:50%}
  .brand-name{color:var(--teal);font-weight:300;text-align:center;line-height:1.15}
  .brand-name .line1{font-size:16px;letter-spacing:.5px;display:block}
  .brand-name .line2{font-size:20.5px;letter-spacing:1px;display:block;font-weight:400}

  .pattern{position:absolute;background:linear-gradient(135deg,#5e8e84 0%,#9cbab3 35%,#d9a99a 55%,#8fa7b8 75%,#4f8176 100%)}
  .pattern.sheet{right:0;top:0;width:320px;height:238px;clip-path:polygon(0 16%,0 0,100% 0,100% 100%,70% 78%,52% 48%,28% 30%,18% 40%,18% 28%,8% 30%)}

  .fold-mark{position:absolute;left:0;height:1px;background:var(--rule)}

  .footer{position:absolute;left:0;bottom:0;width:780px;height:120px}
  .footer svg{position:absolute;inset:0;width:100%;height:100%}
  .footer-cols{position:absolute;left:0;top:51px;width:100%;font-size:8.7px;line-height:10.9px}
  .col{position:absolute;top:0;white-space:nowrap}
  .col .label{font-weight:600;color:var(--teal-soft);letter-spacing:.3px}
  .col .accent{color:var(--teal-soft)}
  .col .strong{font-weight:600;color:var(--teal)}

  .card{position:absolute;left:811px;width:316px;height:204px;background:var(--paper);box-shadow:0 2px 6px rgba(0,0,0,.18);overflow:hidden}
  .card.front{top:401px}
  .card.back{top:641px}
  .pattern.card-art{left:0;top:0;width:316px;height:204px;clip-path:polygon(0 0,100% 0,100% 100%,80% 100%,72% 88%,62% 70%,50% 48%,22% 38%,12% 62%,0 35%)}
  .card-brand{position:absolute;left:20px;top:112px;width:170px;display:flex;flex-direction:column;align-items:center;gap:8px}
  .card-brand .brand-dot{width:34px;height:34px}
  .card-brand .line1{font-size:11.5px}
  .card-brand .line2{font-size:14.5px}

  .back-title{position:absolute;left:22px;top:20px;font-size:11px;color:var(--teal-soft);font-weight:300;letter-spacing:.3px}
  .back-title b{font-weight:600;color:var(--teal)}
  .contact-list{position:absolute;left:22px;top:45px;list-style:none;font-size:11.6px;font-weight:300}
  .contact-list li{display:flex;align-items:center;gap:7px;height:19.8px;white-space:nowrap}
  .contact-list svg{width:15px;height:15px;flex:none}
  .back-band{position:absolute;left:0;bottom:0;width:316px;height:98px}
  .hours{position:absolute;left:22px;top:146px;font-size:11.6px;line-height:14.5px;font-weight:300}
  .hours .label{font-weight:600;color:var(--teal-soft)}
</style>
</head>
<body>

<section class="letterhead">
  <div class="pattern sheet" role="img" aria-label="Dekoratives Dreiecksmuster mit Aquarellflächen in Petrol, Grau und Pastelltönen"></div>

  <div class="brand">
    <span class="brand-dot"></span>
    <div class="brand-name">
      <span class="line1">ZAHNARZTPRAXIS</span>
      <span class="line2">HALVERING &amp; TEAM</span>
    </div>
  </div>

  <span class="fold-mark" style="top:389px;width:22px"></span>
  <span class="fold-mark" style="top:550px;width:15px"></span>
  <span class="fold-mark" style="top:779px;width:22px"></span>

  <footer class="footer">
    <svg viewBox="0 0 780 120" preserveAspectRatio="none"><polygon points="0,39 714,39 780,0 780,120 0,120" fill="var(--band)"/></svg>
    <div class="footer-cols">
      <div class="col" style="left:74px">
        <div class="accent">ZAHNARZTPRAXIS</div>
        <div class="strong">HALVERING &amp; TEAM</div>
        <div>Lindenweg 14</div>
        <div>48155 Tannhausen</div>
      </div>
      <div class="col" style="left:212px">
        <div class="label">KONTAKT:</div>
        <div>Telefon 05321 48790</div>
        <div>info@zahnarztpraxis-tannhausen.de</div>
        <div>www.zahnarztpraxis-tannhausen.de</div>
      </div>
      <div class="col" style="left:409px">
        <div class="label">BANKVERBINDUNG:</div>
        <div>IBAN: DE00 0000 0000 0000 0000 00</div>
        <div>BIC: DEXXXXXXXXX</div>
        <div>St.-Nr.: 000/000/0000</div>
      </div>
      <div class="col" style="left:610px">
        <div class="label">ÖFFNUNGSZEITEN:</div>
        <div class="accent">Mo, Mi, Do 08:00 bis 18:30 Uhr</div>
        <div class="accent">Di, Fr 08:00 bis 13:30 Uhr</div>
      </div>
    </div>
  </footer>
</section>

<section class="card front">
  <div class="pattern card-art" role="img" aria-label="Dekoratives Dreiecksmuster mit Aquarellflächen in Petrol, Grau und Pastelltönen"></div>
  <div class="card-brand">
    <span class="brand-dot"></span>
    <div class="brand-name">
      <span class="line1">ZAHNARZTPRAXIS</span>
      <span class="line2">HALVERING &amp; TEAM</span>
    </div>
  </div>
</section>

<section class="card back">
  <svg class="back-band" viewBox="0 0 316 98" preserveAspectRatio="none"><polygon points="0,28 267,28 316,0 316,98 0,98" fill="var(--band)"/></svg>
  <div class="back-title">ZAHNARZTPRAXIS <b>HALVERING &amp; TEAM</b></div>
  <ul class="contact-list">
    <li><svg viewBox="0 0 16 16" fill="none" stroke="var(--teal-soft)" stroke-width="1"><path d="M8 13s4-4 4-7a4 4 0 0 0-8 0c0 3 4 7 4 7z"/><circle cx="8" cy="6" r="1.5"/><path d="M3 13h10"/></svg>Lindenweg 14, 48155 Tannhausen</li>
    <li><svg viewBox="0 0 16 16" fill="none" stroke="var(--teal)" stroke-width="1"><circle cx="8" cy="8" r="7"/><path d="M5.5 4.5l1.5 1.5-1 1c.5 1.2 1.3 2 2.5 2.5l1-1 1.5 1.5-1 1c-2.5-.3-4.7-2.5-5-5z"/></svg>Telefon 05321 48790</li>
    <li><svg viewBox="0 0 16 16" fill="none" stroke="var(--teal-soft)" stroke-width="1"><path d="M15 1L1 7l5 2 2 5z"/><path d="M15 1L6 9"/></svg>info@zahnarztpraxis-tannhausen.de</li>
    <li><svg viewBox="0 0 16 16" fill="none" stroke="var(--teal-soft)" stroke-width="1"><circle cx="8" cy="8" r="7"/><path d="M4 3c1 2 3 2 3 4s-2 2-2 4M10 2c-1 2 1 3 2 4s0 3-1 4"/></svg>www.zahnarztpraxis-tannhausen.de</li>
  </ul>
  <div class="hours">
    <div class="label">ÖFFNUNGSZEITEN:</div>
    <div>Mo, Mi, Do 08:00 bis 18:30 Uhr</div>
    <div>Di, Fr 08:00 bis 13:30 Uhr</div>
  </div>
</section>

</body>
</html>
```